Tallowmere Office Partners needs a new interactive and interesting website

We need an interesting, professional, modern and functional company website for Tallowmere Office Partners - a young IT Services company based out of Chennai, India.

Tallowmere Office Partners is a fully owned subsidiary of Hollin Cellarworks, one of the world's leading direct to consumer wine merchant.

We already have a registered company logo which must feature in the website.

We conceive, design, develop, test, implement and support IT solutions across the entire Hollin Cellarworks IT landscape. For ex : We currently run about 25 e-commerce websites for Hollin Cellarworks on KVM and Dot Net.

We would like to see our corporate colors used in the website. (Burgundy wine and wine green - source: www.tallowmereop.example)

We are looking at this website to communicate a fun, friendly and professionally managed company - reaching out to career seekers, prospective customers and general public.

For reference - The company name 'Tallowmere' is an inspiration from the Hollin Cellarworks lineage.

The second image with the world map is stickered on our main entrance to the office, I am not sure where this can be used -just putting it out there..
Updates

Please note that there are only a few more days to submit designs for this contest  !

I would appreciate if you can help posting your designs in time for our review and consideration.

Thanks.

Reason: Thanks for your inputs. We have a number of designers and a lot to digest and work with in the past few days. There has been a rush of new designs in the last few days Hence we will require more time to process these and make our decision. Hence i am requesting the contest to be open for more days. Regards, Suresh

Target Market(s)

Prospective job seekers who want to know more about the company and also wish to apply for a job vacancy
People wanting to know more about the company in general and our progress
People who want to see what we offer and how we can help them too - prospective customers
Companies that are interested in our IT Captive journey and are looking for a business opportunity

Industry/Entity Type

E-Commerce

Requirements
Must have
• Log In/ Register facility acting as a Single Sign on for Intranet (Employees)

Facility to post job vacancies (with an expiry date) and enable people to apply for a role and upload their CV/Resume.

Facility to Review Job applications

Facility for website visitors to contact Tallowmere Office Partners via an online 'Contact Us' form with a split of job seekers and business opportunities

Gallery facility to upload pictures regarding company events
Nice to have
• Less Cluttered and contemporary design
Some Wine/Vineyard inspirations will be good but not too much, the company is an IT services company

```html
<!DOCTYPE html>
<html lang="en">
<head>
<meta charset="utf-8">
<title>Tallowmere Office Partners</title>
<link href="https://fonts.googleapis.com/css2?family=PT+Sans:wght@400;700&family=Arimo:wght@400;700&display=swap" rel="stylesheet">
<style>
:root{
  --wine:#8a0f45;
  --green:#8bae2e;
  --ink:#333;
  --muted:#666;
  --rule:#ddd;
  --band:#e8e8e8;
  --footer:#2a2a2a;
}
*{box-sizing:border-box;margin:0;padding:0}
html,body{width:975px;height:1200px;overflow:hidden;background:#fff}
body{position:relative;font-family:"Arimo",Arial,sans-serif;color:var(--ink);font-size:10px}
.abs{position:absolute}
h2{font-family:"PT Sans",sans-serif;font-weight:400;font-size:18px;color:#444;text-transform:uppercase;white-space:nowrap}
.logo{left:116px;top:18px;width:134px;height:67px;background:var(--wine);color:#fff;font-weight:700;display:flex;flex-direction:column;justify-content:center;padding-left:14px;line-height:1.15}
.logo .name{font-size:15px}
.logo .sub{font-size:9.5px}
.social{left:604px;top:33px;display:flex;gap:6.7px}
.social span{width:26px;height:26px;border-radius:50%;border:2px solid #e5e5e5;box-shadow:0 1px 2px rgba(0,0,0,.25)}
.nav{left:116px;top:103px;width:746px;height:35px;background:linear-gradient(#a9c84d,#87a92b);border:1px solid #7b9a25;display:flex}
.nav a{color:#fff;font-weight:700;font-size:10.5px;text-decoration:none;display:flex;align-items:center;justify-content:center;border-right:1px solid #7f9d2a}
.nav a.active{background:linear-gradient(#7d8a34,#66722a)}
.search{position:absolute;left:529px;top:5px;width:212px;height:23px;background:#f8f8f0;border:1px solid #c9d79b;border-radius:2px}
.search i{position:absolute;right:0;top:0;width:26px;height:21px;background:#7c9828}
.hero{left:116px;top:152px;width:745px;height:294px;background:linear-gradient(100deg,#d8cfc4,#b7a59a 40%,#c4cfda 65%,#e7e3de)}
.hero-shadow{left:130px;top:446px;width:717px;height:36px;background:radial-gradient(ellipse at 50% 0,rgba(0,0,0,.14),transparent 70%)}
.arrow{top:286px;width:20px;height:26px;background:rgba(255,255,255,.75)}
.dots{left:440px;top:427px;width:96px;height:19px;background:#f1f1f1;border-radius:6px 6px 0 0;display:flex;justify-content:center;align-items:center;gap:6px}
.dots span{width:9px;height:9px;border-radius:50%;background:#888}
.dots span.on{background:var(--wine)}
.rule{height:1px;background:var(--rule)}
.pager{display:flex;gap:2px}
.pager span{width:17px;height:17px;background:#222;color:#e8a21b;font-size:9px;display:flex;align-items:center;justify-content:center}
.photo{background:linear-gradient(135deg,#cfd4d8,#6b6e70)}
.copy{font-size:9.5px;line-height:12.4px;color:var(--muted);text-align:justify}
.stack{display:flex;flex-direction:column}
.tag{color:var(--wine);font-size:10.5px}
.svc-list{list-style:none;font-size:9.5px;color:#333}
.svc-list li{display:flex;align-items:center;height:28px}
.svc-list li::before{content:"";width:8px;height:8px;border-radius:50%;background:#222;margin:0 10px 0 3px}
.opp{left:366px;width:245px;height:56px}
.opp .date{position:absolute;left:0;top:0;width:55px;height:55px;border-radius:50%;background:var(--wine);color:#fff;font-family:"PT Sans",sans-serif;font-size:16px;line-height:19px;text-align:center;padding-top:9px}
.opp .t,.opp .d,.opp .m{position:absolute;left:62px;width:183px;white-space:nowrap;overflow:hidden;text-overflow:ellipsis}
.opp .t{top:10px;font-size:9px;color:#222}
.opp .d{top:28px;font-size:7.5px;color:#777}
.opp .m{top:42px;font-size:8px;color:var(--wine)}
.vsep{width:4px;background:#e2e2e2}
.video{left:634px;top:818px;width:228px;height:184px;background:linear-gradient(120deg,#eef1f3,#b7bdc3 55%,#50555a)}
.play{left:732px;top:890px;width:40px;height:40px;border-radius:50%;background:rgba(60,60,60,.75)}
.bar{left:634px;top:1002px;width:228px;height:12px;background:#eee;border:1px solid #ccc}
.band{left:0;top:1042px;width:975px;height:90px;background:var(--band);border-bottom:3px solid #999}
.clients{left:268px;top:1078px;width:593px;display:flex;justify-content:space-between}
.client{font-family:"PT Sans",sans-serif;font-size:15px;color:var(--wine);white-space:nowrap}
.footer{left:0;top:1154px;width:975px;height:46px;background:var(--footer)}
.flinks{left:116px;top:1163px;color:#fff;font-size:9.5px}
.copyr{left:116px;top:1181px;color:var(--green);font-size:9.5px}
.fsoc{left:752px;top:1168px;display:flex;gap:6px}
.fsoc span{width:22px;height:22px;border-radius:50%;background:#444}
</style>
</head>
<body>
<div class="abs logo"><span class="name">tallowmere</span><span class="sub">Office Partners</span></div>
<div class="abs social" aria-label="Social links">
  <span style="background:#3b5a9a"></span><span style="background:#2aa3dc"></span><span style="background:#d2432f"></span><span style="background:#1d7bb3"></span><span style="background:#c4161c"></span><span style="background:#f06b1c"></span><span style="background:#5b8fc8"></span><span style="background:#c41a1a"></span>
</div>
<nav class="abs nav">
  <a class="active" style="width:94px">HOME</a>
  <a style="width:138px">ABOUT TALLOWMERE</a>
  <a style="width:101px">SERVICES</a>
  <a style="width:97px">CAREERS</a>
  <a style="width:96px;border-right:0">CONTACT</a>
  <div class="search"><i></i></div>
</nav>
<div class="abs hero" role="img" aria-label="Photo of a smiling business team seated at a meeting"></div>
<div class="abs arrow" style="left:116px;width:18px"></div>
<div class="abs arrow" style="left:839px;background:#d8d8d8"><svg width="22" height="26"><path d="M9 8l5 5-5 5" stroke="#fff" stroke-width="2.5" fill="none"/></svg></div>
<div class="abs dots"><span></span><span class="on"></span><span></span></div>
<div class="abs hero-shadow"></div>

<h2 class="abs" style="left:117px;top:487px;font-size:20px">Welcome!</h2>
<div class="abs rule" style="left:116px;top:523px;width:479px"></div>
<div class="abs photo" style="left:116px;top:541px;width:197px;height:169px" role="img" aria-label="Photo of two colleagues working at a laptop"></div>
<div class="abs stack" style="left:320px;top:539px;width:275px">
  <div class="tag">Delivering IT Excellence</div>
  <p class="copy" style="margin-top:11px">Welcome to Tallowmere Office Partners, an emerging provider of global IT consulting and software services. We are part of the Hollin Cellarworks group, a family run business and the world's largest multi-channel home delivery wine merchant...</p>
  <p class="copy" style="margin-top:11px">Nemo enim ipsam voluptatem quia voluptas sit aspernatur aut odit aut fugit,</p>
  <p class="copy" style="margin-top:23px">&nbsp;Services, an emerging provider of global IT consulting and software services. We are part of the Hollin Cellarworks group, a family run business.</p>
</div>

<h2 class="abs" style="left:634px;top:488px">Testimonials</h2>
<div class="abs pager" style="left:825px;top:491px"><span>&lt;</span><span>&gt;</span></div>
<div class="abs rule" style="left:632px;top:523px;width:230px"></div>
<div class="abs photo" style="left:634px;top:544px;width:76px;height:66px;background:linear-gradient(135deg,#e8d6c6,#9a7f6c)" role="img" aria-label="Portrait photo of the client giving the testimonial"></div>
<p class="abs copy" style="left:716px;top:546px;width:145px;height:63px;overflow:hidden">Hollin Cellarworks IT landscape. Current plans to strategically transform this landscape to a single set of global systems.</p>
<p class="abs copy" style="left:632px;top:621px;width:229px">Hollin Cellarworks IT landscape. Current plans to strategically transform this landscape to a single set of global systems are underway, across all locations.</p>
<div class="abs" style="left:632px;top:686px;color:#666">Thanks</div>
<div class="abs" style="left:632px;top:699px;color:var(--green)">Dominic</div>

<div class="abs" style="left:116px;top:737px;width:745px;height:3px;background:#dcdcd4"></div>

<h2 class="abs" style="left:115px;top:762px">Services</h2>
<div class="abs pager" style="left:307px;top:765px"><span>&lt;</span><span>&gt;</span></div>
<div class="abs rule" style="left:116px;top:798px;width:229px"></div>
<p class="abs copy" style="left:116px;top:813px;width:229px;color:#333">The services we provide enable the businesses we support to efficiently manage key functions, including order management.</p>
<ul class="abs svc-list" style="left:116px;top:858px">
  <li>Packaged Applications</li>
  <li>Enterprise Application Integration</li>
  <li>Digital Commerce</li>
  <li>Application Development &amp; Maintenance</li>
  <li>Multiple versions of Orrel KVM</li>
  <li>Maplestone Ledger AX 2009</li>
</ul>

<div class="abs vsep" style="left:357px;top:760px;height:258px"></div>
<div class="abs vsep" style="left:615px;top:760px;height:258px"></div>

<h2 class="abs" style="left:371px;top:762px">Latest Opportunities</h2>
<div class="abs pager" style="left:566px;top:765px"><span>&lt;</span><span>&gt;</span></div>
<div class="abs rule" style="left:371px;top:798px;width:228px"></div>
<div class="abs opp" style="top:806px"><div class="date">Jan<br>07</div><div class="t">Software Developers/Programmer Analysts</div><div class="d">AX We are looking for a AX Software Developer join...</div><div class="m">read more &gt;&gt;</div></div>
<div class="abs opp" style="top:874px"><div class="date">Jan<br>07</div><div class="t">Software Developers/Programmer Analysts</div><div class="d">AX We are looking for a AX Software Developer join...</div><div class="m">read more &gt;&gt;</div></div>
<div class="abs opp" style="top:942px"><div class="date">Jan<br>07</div><div class="t">Software Developers/Programmer Analysts</div><div class="d">AX We are looking for a AX Software Developer join...</div><div class="m">read more &gt;&gt;</div></div>
<svg class="abs" style="left:426px;top:1005px" width="30" height="14"><circle cx="7" cy="7" r="6" fill="#ddd"/><path d="M8 4.5L5.5 7 8 9.5z" fill="#8a0f45"/><circle cx="23" cy="7" r="6" fill="#ddd"/><path d="M22 4.5L24.5 7 22 9.5z" fill="#8a0f45"/></svg>

<h2 class="abs" style="left:633px;top:762px">Recent Events</h2>
<div class="abs pager" style="left:825px;top:765px"><span>&lt;</span><span>&gt;</span></div>
<div class="abs rule" style="left:632px;top:798px;width:230px"></div>
<div class="abs video" role="img" aria-label="Video still of a presenter leading a company meeting"></div>
<div class="abs play"><svg width="40" height="40"><path d="M15 11l15 9-15 9z" fill="#fff"/></svg></div>
<div class="abs bar"><svg width="226" height="10"><path d="M4 2l5 3-5 3z" fill="#111"/><text x="16" y="8" font-size="7" font-family="Arimo" font-weight="700">00:01</text><rect x="45" y="4" width="110" height="2" fill="#333"/><text x="158" y="8" font-size="7" font-family="Arimo" font-weight="700">100 %</text><rect x="190" y="2" width="7" height="6" fill="none" stroke="#111"/><path d="M204 3h2l3-2v8l-3-2h-2z" fill="#111"/></svg></div>

<div class="abs band"></div>
<svg class="abs" style="left:116px;top:1072px" width="24" height="24"><rect x="0" y="2" width="6" height="22" fill="#9ccb3a"/><rect x="8" y="6" width="6" height="18" fill="#4aa3df"/><rect x="16" y="12" width="6" height="12" fill="#f0a12a"/></svg>
<div class="abs" style="left:158px;top:1082px;font-family:'PT Sans',sans-serif;font-size:12px;color:#333">OUR CLIENTS</div>
<div class="abs" style="left:243px;top:1068px;width:1px;height:42px;background:#ccc"></div>
<div class="abs clients">
  <span class="client">Southern Barrel</span>
  <span class="client">Vinoteca Casa</span>
  <span class="client">Cork People</span>
  <span class="client">Hollin Cellarworks</span>
  <span class="client">Ember Wines</span>
</div>

<div class="abs footer"></div>
<div class="abs flinks">Home | About Tallowmere | Services | Careers | Contact</div>
<div class="abs copyr">© 2014 tallowmereop.. All Rights Reserved.</div>
<div class="abs fsoc"><span></span><span></span><span></span><span></span></div>
</body>
</html>
```